Keystone Disability - Social Security Disability Attorneys

Our company is expanding to attract clients nationwide for our social security disability practice. We have a logo, but I am looking for a creative and elegant letterhead that projects an image of being technologically advanced but still professional enough for the legal field. I am looking for the "wow factor" combined with this is still professional enough for a law practice.

Requesting letterhead and business card design
Updates

Had to update and change the logo. The previous logo had a typo. Please send updates with the new logo for consideration. The letterhead and business cards should be professional enough to be used for a law firm. Thanks.

Industry/Entity Type

Law Practice, Law Firm, Healthcare Industry, Government

Colors

Designer to choose colors to be used in the design.

Requirements
Nice to have
• **Please create a vertical design for the business card**

```html
<!DOCTYPE html>
<html lang="en">
<head>
<meta charset="utf-8">
<title>Keystone Disability – Business Card</title>
<link href="https://fonts.googleapis.com/css2?family=Cinzel:wght@400;600&family=Arimo:wght@400&display=swap" rel="stylesheet">
<style>
  :root {
    --stage: #0b0b0c;
    --card: #262729;
    --card-deep: #1f2022;
    --edge-blue: #3f67e0;
    --brand-blue: #4a72e8;
    --mark-orange: #f08a2c;
    --text-light: #e6e7ea;
    --text-muted: #b9bbc0;
    --rule: #3a3b3f;
    --emboss: #3b3c40;
  }
  * { box-sizing: border-box; margin: 0; padding: 0; }
  html, body {
    width: 1200px; height: 820px; overflow: hidden;
    background: var(--stage);
  }
  .stage {
    position: relative; width: 1200px; height: 820px;
    display: flex; align-items: center; justify-content: center; gap: 60px;
  }
  .card {
    position: relative; width: 520px; height: 297px;
    background: linear-gradient(135deg, var(--card) 0%, var(--card-deep) 100%);
    border-left: 4px solid var(--edge-blue);
    border-bottom: 4px solid var(--edge-blue);
    box-shadow: 0 18px 40px rgba(0,0,0,.6);
    overflow: hidden;
  }
  /* Front */
  .brand {
    position: absolute; top: 52px; right: 40px;
    display: flex; align-items: center; gap: 10px;
  }
  .brand-mark {
    width: 14px; height: 14px; border-radius: 50%;
    background: var(--mark-orange); flex: none;
  }
  .brand-name {
    font-family: 'Arimo', sans-serif; font-weight: 400; font-size: 22px;
    color: var(--text-light); line-height: 1;
  }
  .divider {
    position: absolute; left: 28px; right: 28px; top: 138px;
    height: 1px; background: var(--rule);
  }
  .person { position: absolute; left: 28px; top: 152px; }
  .person-name {
    font-family: 'Cinzel', serif; font-weight: 600; font-size: 24px;
    color: var(--brand-blue); letter-spacing: 1px; line-height: 1;
  }
  .person-role {
    font-family: 'Arimo', sans-serif; font-size: 14px; color: var(--text-light);
    margin-top: 3px;
  }
  .person-rule {
    width: 150px; height: 1px; background: var(--rule); margin: 9px 0 8px;
  }
  .contact-list { list-style: none; }
  .contact-item {
    display: flex; align-items: center; gap: 8px;
    font-family: 'Arimo', sans-serif; font-size: 13px; color: var(--text-light);
    line-height: 19px;
  }
  .contact-item svg { width: 12px; height: 12px; flex: none; }
  .accent { color: var(--brand-blue); }
  .address {
    position: absolute; right: 28px; top: 170px; text-align: right;
    font-family: 'Arimo', sans-serif; font-size: 12.5px; color: var(--text-muted);
    line-height: 17px;
  }
  /* Back */
  .card-back {
    display: flex; align-items: center; justify-content: center;
  }
  .back-brand { display: flex; align-items: center; gap: 14px; }
  .back-mark {
    width: 30px; height: 30px; border-radius: 50%; background: var(--emboss);
  }
  .back-name {
    font-family: 'Arimo', sans-serif; font-weight: 400; font-size: 28px;
    color: var(--emboss);
  }
</style>
</head>
<body>
<main class="stage">
  <section class="card card-front" aria-label="Business card front">
    <div class="brand">
      <div class="brand-mark"></div>
      <div class="brand-name">Keystone Disability</div>
    </div>
    <div class="divider"></div>
    <div class="person">
      <div class="person-name">DANIEL AVERY</div>
      <div class="person-role">Managing Director</div>
      <div class="person-rule"></div>
      <ul class="contact-list">
        <li class="contact-item">
          <svg viewBox="0 0 12 12" aria-hidden="true"><path d="M2.5 1 L4.5 1 L5.3 3.4 L4 4.4 C4.6 5.8 6.2 7.4 7.6 8 L8.6 6.7 L11 7.5 L11 9.5 C11 10.3 10.3 11 9.5 11 C5 11 1 7 1 2.5 C1 1.7 1.7 1 2.5 1 Z" fill="var(--brand-blue)"/></svg>
          055-274 310 862
        </li>
        <li class="contact-item">
          <svg viewBox="0 0 12 12" aria-hidden="true"><rect x="0.5" y="2" width="11" height="8" fill="var(--brand-blue)"/><path d="M0.5 2 L6 6.5 L11.5 2" fill="none" stroke="var(--card)" stroke-width="1"/></svg>
          hello@keystonelaw.example
        </li>
        <li class="contact-item">
          <svg viewBox="0 0 12 12" aria-hidden="true" fill="none" stroke="var(--brand-blue)" stroke-width="1.1"><circle cx="6" cy="6" r="5"/><ellipse cx="6" cy="6" rx="2.2" ry="5"/><path d="M1 6 H11 M2 3.3 H10 M2 8.7 H10"/></svg>
          <span>www.<span class="accent">keystonelaw</span>.example</span>
        </li>
      </ul>
    </div>
    <div class="address">421, Address line goes here<br>45452, Country Name</div>
  </section>

  <section class="card card-back" aria-label="Business card back">
    <div class="back-brand">
      <div class="back-mark"></div>
      <div class="back-name">Keystone Disability</div>
    </div>
  </section>
</main>
</body>
</html>
```